Spanish Student Needs a Cover for his PhD Dissertation

Hi everyone :) So, I'm a Corneal surgeon currently finishing my PhD, with a dissertation focused on the evaluation of quality of life in patients affected by a disease called Keratoconus. Just so you know, Keratoconus is a condition in which the cornea (the frontal part of the way) gets thin and bulgy and it decreases vision. What I did during my PhD was designing a questionnaire for evaluating quality of life in this kind of patients.
I need to design a hard cover for my dissertation, which is 200 sheets long. I like kind of minimalistic and geometric designs but I am totally open to suggestions. What needs to be in the cover is the name of the dissertation "Diseño, desarrollo y validación de una encuesta para evaluar el compromiso visual y emocional subjetivos en pacientes con Queratocono" and my name, "Iñigo Zabaleta". The other thing that needs to go there is the logo of my university (Universidad de Montealto). Aside from that, anything else is up to the designer. It would be important to use the kind of "red" color I am using in the dissertation. I am attaching the frontal page of my dissertation so you know what kind of design and colors I am using.
In the back part, of the cover, there should be this small inscription: "Iñigo Zabaleta, MD, es un Oftalmólogo Subespecialista en Cirugía Refractiva de la Universidad Católica Mirandina (Colombia) y la Universidad de Montealto (España). Actualmente se desempeña como miembro del Departamento de Córnea y Cirugía Refractiva de la Clínica de Oftalmología Los Robles y como director de su propia compañía de emprendimiento médico Silver Heron Surgical". Please leave a space to place my picture; I will have it taken this week so I don't have it right now, you can just leave the blank spot and I will include it later
The size of the pages is standard "letter" size.
Thanks a lot!

Target Market(s)

PhD Scholars

Font styles to use
Serif

Requirements
Must have
• The "red" color I use on my font. It must be formal but "young".
Nice to have
• I like to keep the design clean, kind of "formal with a young" touch so to speak. I really like gray colors, so it would be nice to have broad areas of gray. I love geometrical designs.
I have uploaded a very early version a friend of mine made (it even had a different title); this can be a starting point for you to work on, but I am more than open to suggestions and new ideas.
Should not have
• Please don't use my whole name, Iñigo Zabaleta is fine. I don't like ALL CAPITALS.

```html
<!DOCTYPE html>
<html lang="es">
<head>
<meta charset="utf-8">
<title>Cubierta de tesis doctoral – Iñigo Zabaleta</title>
<link rel="stylesheet" href="https://fonts.googleapis.com/css2?family=Noto+Serif:wght@400;700&display=swap">
<style>
  :root {
    --backdrop: #e6e6e6;
    --paper: #f4f4f4;
    --rose: #c8466b;
    --rose-deep: #b4375c;
    --charcoal: #3a3a3a;
    --charcoal-dark: #2b2b2b;
    --ink: #1e1e1e;
    --white: #ffffff;
    --portrait-slot: #e2e2e2;
  }
  * { box-sizing: border-box; margin: 0; padding: 0; }
  html, body {
    width: 1200px; height: 959px; overflow: hidden;
    background: var(--backdrop);
    font-family: "Noto Serif", serif;
  }
  .spread {
    position: absolute; left: 40px; top: 130px;
    width: 1120px; height: 699px;
    display: flex;
    box-shadow: 0 12px 30px rgba(0,0,0,0.18);
  }
  .cover { position: relative; width: 540px; height: 699px; overflow: hidden; background: var(--paper); }
  .cover svg.surface { position: absolute; inset: 0; }
  .spine {
    position: relative; width: 40px; height: 699px;
    background: var(--rose-deep);
    color: var(--white);
  }
  .spine-text {
    position: absolute; left: 50%;
    writing-mode: vertical-rl;
    transform: translateX(-50%);
    white-space: nowrap;
  }
  .spine-author { top: 60px; font-size: 17px; }
  .spine-university { bottom: 60px; font-size: 12px; font-weight: 700; }

  /* Shared marks */
  .school-mark {
    position: absolute; display: flex; align-items: center; gap: 8px;
    font-size: 13px; font-weight: 700; color: var(--charcoal-dark);
    white-space: nowrap;
  }
  .school-mark .dot { width: 10px; height: 10px; background: var(--rose); }
  .university-mark {
    position: absolute; display: flex; flex-direction: column; align-items: center; gap: 8px;
    font-size: 13px; font-weight: 700; color: var(--ink);
    white-space: nowrap;
  }
  .university-mark .seal {
    width: 54px; height: 54px; border-radius: 50%;
    border: 2px solid var(--ink);
  }

  /* Front cover */
  .front .school-mark { left: 36px; top: 150px; transform: rotate(-7deg); transform-origin: left center; }
  .front .university-mark { right: 40px; top: 36px; transform: rotate(-7deg); }
  .title-block {
    position: absolute; left: 40px; top: 232px; width: 470px;
    color: var(--white);
    transform: rotate(-7.4deg); transform-origin: left top;
  }
  .title { font-size: 17px; font-weight: 400; line-height: 1.32; }
  .title-rule { width: 70px; height: 2px; background: var(--white); margin: 20px 0 10px 10px; }
  .author { font-size: 13px; margin-left: 10px; }

  /* Back cover */
  .portrait-slot {
    position: absolute; left: 200px; top: 190px;
    width: 140px; height: 140px; border-radius: 50%;
    background: var(--portrait-slot);
  }
  .biography {
    position: absolute; left: 55px; top: 360px; width: 430px;
    color: var(--white); text-align: center;
    font-size: 12px; line-height: 1.5;
    transform: rotate(-14deg); transform-origin: center;
  }
  .back .university-mark { left: 80px; top: 582px; transform: rotate(-14deg); }
  .back .school-mark { left: 300px; top: 560px; transform: rotate(-14deg); transform-origin: left center; }
</style>
</head>
<body>
  <main class="spread">
    <!-- Back cover -->
    <section class="cover back">
      <svg class="surface" width="540" height="699" viewBox="0 0 540 699">
        <path d="M0 220 Q270 160 540 70 L540 260 Q270 330 0 400 Z" fill="var(--rose-deep)"/>
        <path d="M0 400 Q270 330 540 260 L540 430 Q270 520 0 570 Z" fill="var(--charcoal)"/>
      </svg>
      <div class="portrait-slot" role="img" aria-label="Espacio reservado para la fotografía del autor"></div>
      <p class="biography">“Iñigo Zabaleta, MD, es un Oftalmólogo Subespecialista en Cirugía Refractiva de la Universidad Católica Mirandina (Colombia) y la Universidad de Montealto (España). Actualmente se desempeña como miembro del Departamento de Córnea y Cirugía Refractiva de la Clínica de Oftalmología Los Robles y como director de su propia compañía de emprendimiento médico Silver Heron Surgical”.</p>
      <div class="university-mark"><span class="seal"></span><span>Universidad de Montealto</span></div>
      <div class="school-mark"><span class="dot"></span><span>Escuela de Doctorado Montealto</span></div>
    </section>

    <!-- Spine -->
    <section class="spine">
      <span class="spine-text spine-author">Iñigo Zabaleta</span>
      <span class="spine-text spine-university">Universidad de Montealto</span>
    </section>

    <!-- Front cover -->
    <section class="cover front">
      <svg class="surface" width="540" height="699" viewBox="0 0 540 699">
        <defs>
          <radialGradient id="cornea-glow" cx="0.62" cy="0.55" r="0.6">
            <stop offset="0" stop-color="#8a8a8a"/>
            <stop offset="0.55" stop-color="#4a4a4a"/>
            <stop offset="1" stop-color="#2e2e2e"/>
          </radialGradient>
        </defs>
        <path d="M0 205 L540 130 L540 300 Q270 350 0 420 Z" fill="var(--rose)"/>
        <path class="cover-photo" d="M0 420 Q270 350 540 300 L540 699 L0 699 Z" fill="url(#cornea-glow)" role="img" aria-label="Fotografía en blanco y negro de una córnea cónica vista de perfil"/>
      </svg>
      <div class="university-mark"><span class="seal"></span><span>Universidad de Montealto</span></div>
      <div class="school-mark"><span class="dot"></span><span>Escuela de Doctorado Montealto</span></div>
      <div class="title-block">
        <h1 class="title">“Diseño, desarrollo y validación de una encuesta para evaluar el compromiso visual y emocional subjetivos en pacientes con Queratocono”</h1>
        <div class="title-rule"></div>
        <p class="author">Iñigo Zabaleta</p>
      </div>
    </section>
  </main>
</body>
</html>
```